Small Accounting Practice needs something creative

We need a business card design for a new small accounting practice based in Perth, Australia. The name of the practice is 'Kowra Ledger Partners Pty Ltd'. We providing Tax, Bookkeeping and Accounting services. Our target are individuals and small businesses. We want the design to be simply and creative. Also, we can the design can help us to gain people's trust.

Target Market(s)

Individuals and small businesses.

Industry/Entity Type

Accounting

Colors

Designer to choose colors to be used in the design.

```html
<!DOCTYPE html>
<html lang="en">
<head>
<meta charset="utf-8">
<title>Kowra Ledger Partners – Business Card</title>
<link rel="stylesheet" href="https://fonts.googleapis.com/css2?family=Questrial&display=swap">
<style>
  :root {
    --backdrop: #c9f5dc;
    --card-white: #ffffff;
    --brand-blue: #0d3fd0;
    --brand-blue-deep: #0a2aa8;
    --brand-blue-light: #1d56e6;
    --ink-grey: #4a4f57;
    --accent-cyan: #7fe9ff;
    --accent-white: #e9f3ff;
  }
  * { box-sizing: border-box; margin: 0; padding: 0; }
  html, body {
    width: 1200px; height: 960px; overflow: hidden;
    background: var(--backdrop);
    font-family: "Questrial", "Century Gothic", sans-serif;
  }
  .canvas { position: relative; width: 1200px; height: 960px; }

  .card {
    position: absolute;
    width: 540px; height: 330px;
    border-radius: 30px;
    box-shadow: 0 10px 30px rgba(20, 80, 60, 0.18);
  }

  /* Front */
  .card-front {
    left: 70px; top: 520px;
    background: var(--card-white);
  }
  .front-content {
    position: absolute; left: 96px; top: 92px;
    display: flex; flex-direction: column; align-items: flex-start;
  }
  .brand-name {
    color: var(--brand-blue);
    line-height: 1;
    text-transform: uppercase;
    font-weight: 400;
    white-space: nowrap;
  }
  .brand-name .brand-main {
    display: block;
    font-size: 46px; letter-spacing: 1.5px;
  }
  .brand-name .brand-sub {
    display: block;
    font-size: 15px; letter-spacing: 1.5px;
    margin-top: 8px;
    color: var(--ink-grey);
  }
  .holder { margin-top: 22px; white-space: nowrap; }
  .holder-name {
    color: var(--brand-blue);
    font-size: 22px; letter-spacing: 1px; line-height: 1.1;
    text-transform: uppercase;
  }
  .holder-role {
    color: var(--ink-grey);
    font-size: 15px; margin-top: 4px;
  }

  /* Back */
  .card-back {
    left: 600px; top: 110px;
    background: linear-gradient(170deg, var(--brand-blue-light) 0%, var(--brand-blue) 55%, var(--brand-blue-deep) 100%);
    color: var(--accent-white);
  }
  .services {
    position: absolute; left: 0; right: 0; top: 118px;
    text-align: center;
    color: var(--accent-cyan);
    font-size: 16px; letter-spacing: 1.2px;
    text-transform: uppercase;
  }
  .contact {
    position: absolute; right: 34px; bottom: 34px;
    text-align: right;
    font-size: 15px; letter-spacing: 0.5px;
  }
  .registration {
    font-size: 13px; letter-spacing: 1px;
    text-transform: uppercase;
    margin-bottom: 8px;
  }
  .contact-line {
    display: flex; align-items: center; justify-content: flex-end; gap: 14px;
    white-space: nowrap;
  }
  .contact-item { display: inline-flex; align-items: center; gap: 6px; }
  .contact-icon { width: 16px; height: 16px; flex: none; }
</style>
</head>
<body>
<main class="canvas">

  <section class="card card-back" aria-label="Business card back">
    <p class="services">Tax, Bookkeeping and Accounting Services</p>
    <div class="contact">
      <p class="registration">Registered ASIC Agent 48071</p>
      <div class="contact-line">
        <span class="contact-item">
          <svg class="contact-icon" viewBox="0 0 16 16" aria-hidden="true">
            <rect x="1.5" y="3" width="13" height="10" rx="1.5" fill="none" stroke="var(--accent-cyan)" stroke-width="1.6"/>
            <path d="M2 4 L8 9 L14 4" fill="none" stroke="var(--accent-cyan)" stroke-width="1.4"/>
          </svg>
          tomas@kowraledger.com.au
        </span>
        <span class="contact-item">
          <svg class="contact-icon" viewBox="0 0 16 16" aria-hidden="true">
            <rect x="0.5" y="0.5" width="15" height="15" rx="2" fill="var(--accent-white)"/>
            <path d="M5 3.5 L6.6 3.5 L7.4 6 L6.3 7 C6.9 8.3 7.7 9.1 9 9.7 L10 8.6 L12.5 9.4 L12.5 11 C12.5 11.8 11.8 12.5 11 12.5 C7.2 12.2 3.8 8.8 3.5 5 C3.5 4.2 4.2 3.5 5 3.5 Z" fill="var(--brand-blue)"/>
          </svg>
          0491 570 156
        </span>
      </div>
    </div>
  </section>

  <section class="card card-front" aria-label="Business card front">
    <div class="front-content">
      <h1 class="brand-name">
        <span class="brand-main">Kowra Ledger</span>
        <span class="brand-sub">Partners Pty Ltd</span>
      </h1>
      <div class="holder">
        <p class="holder-name">Tomas Reyner</p>
        <p class="holder-role">Accountant &amp; Small Business Consultant</p>
      </div>
    </div>
  </section>

</main>
</body>
</html>
```